Business card design for new eCommerce site focusing on integrity and strong businsess tactics

We need a business card that will stand out and be memorable. Something with color that matches our company logo colors. Think high end version of Tallyhop. There are 2 logos provided. The parent company is called Brightwell Craft Partners and we are presenting a new and very exciting eCommerce site called KestrelTradeHub.example.

Target Market(s)

Our target markets are in the Activities, Food and Beverage, Health and Beauty

Industry/Entity Type

Marketing

Contact Information for Business Card

We have 4 members that need cards...I will provide all info to the winner of the design contest
Business Address is
47390 West 63rd Lane, Suite K204
Phoenix AZ 85061

Font styles to use
Serif
Sans Serif

Colors

Designer to choose colors to be used in the design.

Requirements
Must have
• The card must be memorable...should be unique in design but must exude integrity and be playful .
• I have provided several colors or our parent company...please feel free to use which ever
Nice to have
• I will leave this up to you. Feel free to use other images of your choosing that wraps around our client.....Activities, Dining, Health, Beauty
Should not have
• just dont be boring

```html
<!DOCTYPE html>
<html lang="en">
<head>
<meta charset="utf-8">
<title>Brightwell Craft Partners – Business Card</title>
<link rel="stylesheet" href="https://fonts.googleapis.com/css2?family=Open+Sans:wght@400;600;700&display=swap">
<style>
  :root {
    --backdrop: #3b3330;
    --card: #121212;
    --card-edge: #1c1c1c;
    --ink-white: #f2f2f2;
    --ink-grey: #8c8c8c;
    --ink-silver: #a9a9a9;
    --accent-blue: #2a8fd0;
    --accent-green: #6cc13a;
    --rule: #d9d9d9;
  }
  * { box-sizing: border-box; margin: 0; padding: 0; }
  html, body { width: 1200px; height: 864px; overflow: hidden; }
  body {
    background: var(--backdrop);
    font-family: "Open Sans", Arial, sans-serif;
    position: relative;
  }
  .card {
    position: absolute;
    width: 500px;
    height: 290px;
    background: var(--card);
    border: 1px solid var(--card-edge);
    box-shadow: 0 10px 28px rgba(0,0,0,0.45);
  }
  /* Front */
  .card-front { left: 80px; top: 110px; }
  .front-brand {
    position: absolute;
    left: 0; right: 0; top: 96px;
    display: flex; align-items: center; justify-content: center; gap: 14px;
  }
  .front-brand .mark {
    width: 40px; height: 40px; border-radius: 50%;
    background: #2a2a2a;
  }
  .front-brand .name {
    color: var(--ink-silver);
    font-weight: 700;
    font-size: 27px;
  }
  .front-url {
    position: absolute;
    left: 0; right: 0; top: 172px;
    text-align: center;
    color: var(--ink-grey);
    font-size: 13px;
    letter-spacing: 3px;
  }
  /* Back */
  .card-back { left: 620px; top: 440px; }
  .person { position: absolute; left: 30px; top: 70px; }
  .person .full-name {
    color: var(--accent-blue);
    font-weight: 700; font-size: 14px; text-transform: uppercase;
  }
  .person .role {
    color: var(--accent-green);
    font-size: 14px; text-transform: uppercase;
  }
  .contacts { position: absolute; left: 30px; top: 120px; list-style: none; }
  .contacts li {
    display: flex; align-items: center; gap: 8px;
    color: var(--ink-white); font-size: 13px; line-height: 18px;
  }
  .contacts svg { width: 11px; height: 11px; fill: var(--accent-blue); flex: none; }
  .rule {
    position: absolute; left: 30px; right: 30px; top: 200px;
    height: 1px; background: var(--rule);
  }
  .back-brand {
    position: absolute; right: 26px; top: 78px;
    text-align: right;
  }
  .back-brand .line {
    display: flex; align-items: center; justify-content: flex-end; gap: 8px;
  }
  .back-brand .mark {
    width: 22px; height: 22px; border-radius: 50%; background: var(--accent-blue);
  }
  .back-brand .name {
    color: var(--accent-green); font-weight: 700; font-size: 17px;
  }
  .back-brand .tagline {
    color: var(--ink-grey); font-size: 10px; letter-spacing: 0.5px; margin-top: 2px;
  }
  .address {
    position: absolute; right: 30px; top: 212px;
    text-align: right; color: var(--ink-white); font-size: 13px; line-height: 19px;
    font-style: normal;
  }
</style>
</head>
<body>
  <section class="card card-front" aria-label="Card front">
    <div class="front-brand">
      <span class="mark"></span>
      <span class="name">Brightwell Craft Partners</span>
    </div>
    <p class="front-url">www.kestreltradehub.example</p>
  </section>

  <section class="card card-back" aria-label="Card back">
    <div class="person">
      <p class="full-name">Dana Merrow</p>
      <p class="role">CEO/Founder</p>
    </div>
    <ul class="contacts">
      <li><svg viewBox="0 0 12 12"><path d="M2 1h3l1 3-2 1a7 7 0 0 0 3 3l1-2 3 1v3c0 1-1 1-1 1C5 11 1 7 1 2c0 0 0-1 1-1z"/></svg>555 014 2738</li>
      <li><svg viewBox="0 0 12 12"><path d="M3 0h6v12H3zM4 1v8h4V1z"/></svg>555 019 4462</li>
      <li><svg viewBox="0 0 12 12"><path d="M0 2h12v8H0zM1 3l5 4 5-4z"/></svg>dana@kestreltradehub.example</li>
      <li><svg viewBox="0 0 12 12"><circle cx="6" cy="6" r="6"/></svg>www.kestreltradehub.example</li>
    </ul>
    <div class="rule"></div>
    <div class="back-brand">
      <div class="line"><span class="mark"></span><span class="name">KestrelTradeHub.example</span></div>
      <p class="tagline">Activities-Dining-Health-Beauty</p>
    </div>
    <address class="address">47390 West 63rd Lane<br>Suite K204<br>Phoenix AZ 85061</address>
  </section>
</body>
</html>
```